Plakat-Design für IT-Firma
Zielgruppe
Wir sind eine junge dynamische B2B IT Firma, die für ihre Kunden (kleine & mittelständische Unternehmen) einen Full-Service (Server, Computer, Telefonanlagen) bietet. Wir kümmern uns um alles, was einen Stecker hat.
Aufgabenstellung
Wir benötigen eine Datei für eine Plakatwerbung, die auf großen LED Screens am Straßenrand zu sehen sein wird (Seitenverhältnis 672 ×432). Außerdem möchten wir diese auch als PDF veröffentlichen.
Wir möchten, dass unser Logo zusehen ist sowie folgender Text:
'Sie sorgen für die Abläufe im Unternehmen.
Wir für die reibungslose IT.
kolvanda-tec.de'
Die Farben sollten Blau, Orange und Grau sein, wie auf unserer Webseite kolvanda-tec.de zu sehen ist.
Wir sind offen, für kreative Ideen, auch leichte Abänderungen der Wortlaute können wir uns vorstellen.
Es ist wichtig, dass es kurz und prägnant ist. Dass es an der roten Ampelphase, beim kurzen Vorbeifahren in Erinnerung bleibt, optisch Aufmerksamkeit erregt und neugierig macht.
Wir benötigen folgende Formate:
1. JPG Datei in 672 ×432
2. Bilddatei in mind. Full HD
3. PDF

```html
<!DOCTYPE html>
<html lang="de">
<head>
<meta charset="utf-8">
<title>Kolvanda Tec – LED-Plakat</title>
<link rel="stylesheet" href="https://fonts.googleapis.com/css2?family=Open+Sans:wght@400;600;700&display=swap">
<style>
  :root {
    --stage: #e9e9e7;
    --navy-deep: #0b1a2a;
    --navy-mid: #1c3550;
    --steel: #4d6d8c;
    --orange: #e0663a;
    --orange-soft: rgba(224, 102, 58, 0);
    --white: #ffffff;
    --panel-grey: #eef0f2;
    --brand-blue: #2c5b80;
  }
  * { margin: 0; padding: 0; box-sizing: border-box; }
  html, body {
    width: 1200px;
    height: 1052px;
    overflow: hidden;
    background: var(--stage);
    font-family: "Open Sans", Arial, sans-serif;
  }
  .poster {
    position: absolute;
    left: 0;
    top: 140px;
    width: 1200px;
    height: 771px;
    overflow: hidden;
    background: var(--panel-grey);
  }
  .poster__photo {
    position: absolute;
    left: 0;
    top: 0;
    width: 1200px;
    height: 731px;
    background:
      radial-gradient(ellipse 420px 520px at 960px 330px, rgba(150, 175, 200, 0.55), rgba(150, 175, 200, 0) 70%),
      linear-gradient(180deg, #2a4562 0%, var(--navy-mid) 35%, var(--navy-deep) 100%);
  }
  .poster__headline {
    position: absolute;
    left: 74px;
    top: 78px;
    color: var(--white);
    font-weight: 700;
    font-size: 56px;
    line-height: 76px;
    letter-spacing: -0.2px;
  }
  .poster__band {
    position: absolute;
    left: 0;
    top: 450px;
    width: 900px;
    height: 281px;
    background: linear-gradient(90deg, var(--orange) 0%, var(--orange) 62%, var(--orange-soft) 100%);
  }
  .poster__claim {
    position: absolute;
    left: 74px;
    top: 458px;
    color: var(--white);
    font-weight: 700;
    font-size: 56px;
    line-height: 76px;
  }
  .poster__claim-accent {
    position: relative;
    display: inline-block;
  }
  .poster__claim-underline {
    position: absolute;
    left: -4px;
    bottom: -6px;
    width: 96px;
    height: 16px;
  }
  .poster__url {
    position: absolute;
    left: 74px;
    top: 640px;
    color: var(--white);
    font-weight: 400;
    font-size: 40px;
    line-height: 56px;
  }
  .poster__brand-panel {
    position: absolute;
    left: 740px;
    top: 601px;
    width: 460px;
    height: 130px;
    background: linear-gradient(90deg, rgba(238, 240, 242, 0) 0%, var(--panel-grey) 22%);
  }
  .poster__brand {
    position: absolute;
    left: 798px;
    top: 690px;
    color: var(--brand-blue);
    font-weight: 700;
    font-size: 30px;
    line-height: 40px;
    letter-spacing: 2px;
  }
</style>
</head>
<body>
  <main class="poster">
    <div class="poster__photo" role="img" aria-label="Foto: IT-Techniker mit Brille und Tablet in einem Serverraum mit beleuchteten Serverschränken"></div>

    <h1 class="poster__headline">Sie sorgen für<br>die Abläufe im<br>Unternehmen.</h1>

    <div class="poster__band"></div>
    <div class="poster__brand-panel"></div>

    <p class="poster__claim">Wir für die<br>reibungslose <span class="poster__claim-accent">IT.<svg class="poster__claim-underline" viewBox="0 0 96 16" aria-hidden="true"><path d="M3 11 Q 40 4 93 8" fill="none" stroke="#ffffff" stroke-width="4" stroke-linecap="round"/></svg></span></p>

    <p class="poster__url">kolvanda-tec.de</p>

    <p class="poster__brand">KOLVANDA TEC</p>
  </main>
</body>
</html>
```